Vet Project for Web Application

We are developing a web app / forms to allow a Vet to record information when visiting a farm - eg to test animals for TB.
Needs to be clean and fresh, not cluttered.
Using standard web form design elements so that the user don't have to think.
Needs to use elements of the colours from the logo.

We will need a standard template page which we can base each of our webforms on, so we will need
standard web elements (labels, text boxes, radio buttons etc)
data grids
buttons
menus
error messages

Target Market(s)

Vets for farm animals

Number of Pages Required

1 page

Font styles to use
Sans Serif

Requirements
Must have
• Simple form elements. Intuitive. Obvious. Follow the colour pallette in the logo
Should not have
• elements that need instruction to use

```html
<!DOCTYPE html>
<html lang="en">
<head>
<meta charset="utf-8">
<title>HerdCheck – Add Record</title>
<link href="https://fonts.googleapis.com/css2?family=Nunito+Sans:wght@400;600;700;800&display=swap" rel="stylesheet">
<style>
:root{
  --backdrop:#59595b;
  --panel:#ffffff;
  --sidebar:#f2f2f2;
  --brand-blue:#5aa5d6;
  --brand-green:#b5cf5a;
  --ink:#222222;
  --muted:#555555;
  --field-border:#9a9a9a;
  --table-head:#8a8a8b;
  --row-alt:#f4f4f4;
  --divider:#dddddd;
  --error:#c40d0d;
  --trash:#e4531d;
}
*{box-sizing:border-box;margin:0;padding:0}
html,body{width:1038px;height:1200px;overflow:hidden;background:var(--backdrop)}
body{font-family:"Nunito Sans",sans-serif;color:var(--ink)}
.stage{position:absolute;left:0;top:0;width:1718px;height:1987px;transform:scale(.60419);transform-origin:0 0}
.screen{position:absolute;left:114px;width:1500px;height:832px;background:var(--panel);overflow:hidden}
.screen--default{top:128px}
.screen--error{top:1039px}

.sidebar{position:absolute;left:0;top:0;width:241px;height:100%;background:var(--sidebar)}
.brand{position:absolute;left:30px;top:38px;display:flex;align-items:center;gap:8px;font-size:28px;font-weight:700;color:var(--brand-blue);white-space:nowrap;line-height:1}
.brand-dot{width:12px;height:12px;background:var(--brand-green)}
.menu{position:absolute;left:0;top:146px;width:241px;list-style:none}
.menu-item{position:relative;height:62px;display:flex;align-items:center;padding-left:40px;font-size:17px;color:var(--ink);gap:12px}
.menu-item::after{content:"";position:absolute;left:20px;right:25px;bottom:0;border-bottom:1px solid var(--divider)}
.menu-item:last-child::after,.menu-item--active::after{display:none}
.menu-item svg{width:17px;height:17px;fill:none;stroke:#444;stroke-width:1.4}
.menu-item--active{height:52px;background:var(--brand-blue);color:#fff;margin-bottom:10px}
.menu-item--active svg{stroke:#fff}
.menu-item--active::before{content:"";position:absolute;right:0;top:19px;border:7px solid transparent;border-right-color:var(--panel)}

.topbar{position:absolute;left:241px;right:0;top:0;height:76px;background:#fff;box-shadow:0 3px 5px rgba(0,0,0,.06)}
.hamburger{position:absolute;left:36px;top:30px;width:26px;height:20px}
.top-actions{position:absolute;right:26px;top:16px;display:flex;align-items:center;height:42px}
.top-actions .icon{width:28px;height:28px;fill:none;stroke:#888;stroke-width:2.2;margin-right:22px}
.bell{position:relative;margin-right:10px}
.bell .badge{position:absolute;right:18px;top:-4px;width:15px;height:15px;border-radius:50%;background:var(--brand-green);color:#fff;font-size:10px;text-align:center;line-height:15px}
.avatar{width:40px;height:40px;border-radius:50%;background:linear-gradient(#c9d9e6,#5a87b0);margin-right:10px}
.user-name{font-size:17px;margin-right:10px}
.caret{width:0;height:0;border:5px solid transparent;border-top-color:#222;margin-top:6px}

.content{position:absolute;left:281px;top:0;width:1190px}
.title{position:absolute;top:120px;font-size:20px;font-weight:800;letter-spacing:.3px}
.field{position:absolute;width:382px;height:52px;border:1px solid var(--field-border);font-size:14px;color:#444;padding-left:18px;display:flex;align-items:center;background:#fff}
.field--select::after{content:"";position:absolute;right:16px;top:22px;border:5px solid transparent;border-top-color:#222}
.field--invalid{border-color:var(--error);color:var(--error)}
.field--invalid .alert{position:absolute;right:12px;top:15px;width:22px;height:22px}
.tooltip{position:absolute;left:403px;top:156px;width:135px;height:66px;background:var(--error);color:#fff;font-size:14px;line-height:18px;padding:14px 0 0 24px;z-index:2}
.tooltip::before{content:"";position:absolute;left:-8px;top:25px;border:8px solid transparent;border-left:0;border-right-color:var(--error)}
.gender{position:absolute;left:812px;top:158px;font-size:14px;color:#444}
.gender-options{display:flex;gap:28px;margin-top:12px}
.radio{display:flex;align-items:center;gap:10px}
.radio i{width:18px;height:18px;border-radius:50%;background:#888;display:block}
.submit{position:absolute;left:808px;top:305px;width:382px;height:52px;background:var(--brand-green);border:0;color:#fff;font:800 22px "Nunito Sans",sans-serif;letter-spacing:.5px}

.records{position:absolute;left:0;top:395px;width:1190px;border-collapse:collapse;table-layout:fixed;box-shadow:0 3px 6px rgba(0,0,0,.12);font-size:15px}
.records th{height:38px;background:var(--table-head);color:#fff;font-weight:600;border-right:1px solid #a4a4a4}
.records td{height:50px;border-right:1px solid #e4e4e4}
.records th:last-child,.records td:last-child{border-right:0}
.records tbody tr:nth-child(even){background:var(--row-alt)}
.records .l{padding-left:18px}
.records .first{padding-left:30px}
.records .c{text-align:center}
.actions{display:flex;justify-content:center;align-items:center;gap:8px}
.actions svg{width:16px;height:16px}
.actions .sep{width:1px;height:20px;background:#ddd}
.copyright{position:absolute;top:776px;width:1190px;text-align:center;font-size:15px;color:#333}
</style>
</head>
<body>
<div class="stage">

  <section class="screen screen--default">
    <aside class="sidebar">
      <div class="brand"><span>HERDCHECK</span><span class="brand-dot"></span></div>
      <ul class="menu">
        <li class="menu-item menu-item--active"><svg viewBox="0 0 16 16"><path d="M2 8l6-5 6 5M4 7v7h8V7"/></svg>Dashboard</li>
        <li class="menu-item"><svg viewBox="0 0 16 16"><path d="M3 1h7l3 3v11H3zM5 7h6M5 10h6"/></svg>Records</li>
        <li class="menu-item"><svg viewBox="0 0 16 16"><circle cx="8" cy="8" r="6"/><path d="M8 7v4M8 5v.5"/></svg>Information</li>
        <li class="menu-item"><svg viewBox="0 0 16 16"><path d="M8 14L2 8a3.3 3.3 0 016-4 3.3 3.3 0 016 4zM3 8h3l1-2 2 4 1-2h3"/></svg>Health</li>
        <li class="menu-item"><svg viewBox="0 0 16 16"><path d="M2 3h12v8H6l-4 3zM5 6h6M5 8h4"/></svg>Messages</li>
        <li class="menu-item"><svg viewBox="0 0 16 16"><circle cx="8" cy="8" r="2.5"/><circle cx="8" cy="8" r="6" stroke-dasharray="2 1.4"/></svg>Settings</li>
      </ul>
    </aside>
    <header class="topbar">
      <svg class="hamburger" viewBox="0 0 26 20"><path d="M0 2h26M0 10h26M0 18h26" stroke="#444" stroke-width="3"/></svg>
      <div class="top-actions">
        <svg class="icon" viewBox="0 0 28 28"><circle cx="12" cy="12" r="9"/><path d="M19 19l7 7"/></svg>
        <div class="bell"><svg class="icon" viewBox="0 0 28 28"><path d="M6 21V13a8 8 0 0116 0v8l2 2H4zM11 25h6"/></svg><span class="badge">0</span></div>
        <div class="avatar" role="img" aria-label="User profile photo"></div>
        <span class="user-name">Owen Hale</span><span class="caret"></span>
      </div>
    </header>
    <main class="content">
      <h1 class="title">ADD RECORD</h1>
      <div class="field" style="left:1px;top:163px">Vet Name</div>
      <div class="field" style="left:405px;top:163px">Vet Age</div>
      <div class="gender">Gender<div class="gender-options"><span class="radio"><i></i>Male</span><span class="radio"><i></i>Female</span></div></div>
      <div class="field" style="left:1px;top:234px">Weight</div>
      <div class="field" style="left:405px;top:234px">Color</div>
      <div class="field field--select" style="left:808px;top:234px">Number of Animales</div>
      <div class="field" style="left:1px;top:305px">Farm location</div>
      <div class="field" style="left:405px;top:305px">Reason</div>
      <button class="submit">SUBMIT</button>
      <table class="records">
        <colgroup><col style="width:256px"><col style="width:88px"><col style="width:85px"><col style="width:79px"><col style="width:78px"><col style="width:115px"><col style="width:140px"><col style="width:268px"><col style="width:81px"></colgroup>
        <thead><tr><th>Vet Name</th><th>Vet Age</th><th>Gender</th><th>Weight</th><th>Color</th><th>No.of animals</th><th>Location</th><th>Reason</th><th>Action</th></tr></thead>
        <tbody>
          <tr><td class="first">Cookie</td><td class="c">8</td><td class="l">Male</td><td class="c">20</td><td class="l">Brown</td><td class="c">1</td><td class="l">Allentown</td><td class="l">Lorem Ipsum is simply dummy</td><td><div class="actions"><svg viewBox="0 0 16 16" fill="none" stroke="#9cc43c" stroke-width="1.4"><path d="M13 9v5H2V3h5M6 10l1-3 6-6 2 2-6 6z"/></svg><span class="sep"></span><svg viewBox="0 0 16 16" fill="none" stroke="#e4531d" stroke-width="1.6"><path d="M2 4h12M6 4V2h4v2M4 4l1 11h6l1-11M7 7v5M9 7v5"/></svg></div></td></tr>
          <tr><td class="first">Lydia</td><td class="c">12</td><td class="l">Female</td><td class="c">15</td><td class="l">White</td><td class="c">3</td><td class="l">Orlando</td><td class="l">Contrary to popular belief</td><td><div class="actions"><svg viewBox="0 0 16 16" fill="none" stroke="#9cc43c" stroke-width="1.4"><path d="M13 9v5H2V3h5M6 10l1-3 6-6 2 2-6 6z"/></svg><span class="sep"></span><svg viewBox="0 0 16 16" fill="none" stroke="#e4531d" stroke-width="1.6"><path d="M2 4h12M6 4V2h4v2M4 4l1 11h6l1-11M7 7v5M9 7v5"/></svg></div></td></tr>
          <tr><td class="first">Cowles</td><td class="c">5</td><td class="l">Male</td><td class="c">31</td><td class="l">Black</td><td class="c">2</td><td class="l">Miami</td><td class="l">There are many variations of</td><td><div class="actions"><svg viewBox="0 0 16 16" fill="none" stroke="#9cc43c" stroke-width="1.4"><path d="M13 9v5H2V3h5M6 10l1-3 6-6 2 2-6 6z"/></svg><span class="sep"></span><svg viewBox="0 0 16 16" fill="none" stroke="#e4531d" stroke-width="1.6"><path d="M2 4h12M6 4V2h4v2M4 4l1 11h6l1-11M7 7v5M9 7v5"/></svg></div></td></tr>
          <tr><td class="first">Owens</td><td class="c">3</td><td class="l">Female</td><td class="c">25</td><td class="l">White</td><td class="c">6</td><td class="l">Fresno</td><td class="l">It is a long established fact</td><td><div class="actions"><svg viewBox="0 0 16 16" fill="none" stroke="#9cc43c" stroke-width="1.4"><path d="M13 9v5H2V3h5M6 10l1-3 6-6 2 2-6 6z"/></svg><span class="sep"></span><svg viewBox="0 0 16 16" fill="none" stroke="#e4531d" stroke-width="1.6"><path d="M2 4h12M6 4V2h4v2M4 4l1 11h6l1-11M7 7v5M9 7v5"/></svg></div></td></tr>
          <tr><td class="first">Beverly</td><td class="c">1</td><td class="l">Male</td><td class="c">10</td><td class="l">Brown</td><td class="c">5</td><td class="l">Mer Rouge</td><td class="l">Lorem Ipsum is simply dummy</td><td><div class="actions"><svg viewBox="0 0 16 16" fill="none" stroke="#9cc43c" stroke-width="1.4"><path d="M13 9v5H2V3h5M6 10l1-3 6-6 2 2-6 6z"/></svg><span class="sep"></span><svg viewBox="0 0 16 16" fill="none" stroke="#e4531d" stroke-width="1.6"><path d="M2 4h12M6 4V2h4v2M4 4l1 11h6l1-11M7 7v5M9 7v5"/></svg></div></td></tr>
          <tr><td class="first">Plumley</td><td class="c">20</td><td class="l">Female</td><td class="c">30</td><td class="l">Black</td><td class="c">3</td><td class="l">Sophia</td><td class="l">Contrary to popular belief</td><td><div class="actions"><svg viewBox="0 0 16 16" fill="none" stroke="#9cc43c" stroke-width="1.4"><path d="M13 9v5H2V3h5M6 10l1-3 6-6 2 2-6 6z"/></svg><span class="sep"></span><svg viewBox="0 0 16 16" fill="none" stroke="#e4531d" stroke-width="1.6"><path d="M2 4h12M6 4V2h4v2M4 4l1 11h6l1-11M7 7v5M9 7v5"/></svg></div></td></tr>
        </tbody>
      </table>
      <p class="copyright">Copyright © 2022 All Rights Reserved</p>
    </main>
  </section>

  <section class="screen screen--error">
    <aside class="sidebar">
      <div class="brand"><span>HERDCHECK</span><span class="brand-dot"></span></div>
      <ul class="menu">
        <li class="menu-item menu-item--active"><svg viewBox="0 0 16 16"><path d="M2 8l6-5 6 5M4 7v7h8V7"/></svg>Dashboard</li>
        <li class="menu-item"><svg viewBox="0 0 16 16"><path d="M3 1h7l3 3v11H3zM5 7h6M5 10h6"/></svg>Records</li>
        <li class="menu-item"><svg viewBox="0 0 16 16"><circle cx="8" cy="8" r="6"/><path d="M8 7v4M8 5v.5"/></svg>Information</li>
        <li class="menu-item"><svg viewBox="0 0 16 16"><path d="M8 14L2 8a3.3 3.3 0 016-4 3.3 3.3 0 016 4zM3 8h3l1-2 2 4 1-2h3"/></svg>Health</li>
        <li class="menu-item"><svg viewBox="0 0 16 16"><path d="M2 3h12v8H6l-4 3zM5 6h6M5 8h4"/></svg>Messages</li>
        <li class="menu-item"><svg viewBox="0 0 16 16"><circle cx="8" cy="8" r="2.5"/><circle cx="8" cy="8" r="6" stroke-dasharray="2 1.4"/></svg>Settings</li>
      </ul>
    </aside>
    <header class="topbar">
      <svg class="hamburger" viewBox="0 0 26 20"><path d="M0 2h26M0 10h26M0 18h26" stroke="#444" stroke-width="3"/></svg>
      <div class="top-actions">
        <svg class="icon" viewBox="0 0 28 28"><circle cx="12" cy="12" r="9"/><path d="M19 19l7 7"/></svg>
        <div class="bell"><svg class="icon" viewBox="0 0 28 28"><path d="M6 21V13a8 8 0 0116 0v8l2 2H4zM11 25h6"/></svg><span class="badge">0</span></div>
        <div class="avatar" role="img" aria-label="User profile photo"></div>
        <span class="user-name">Owen Hale</span><span class="caret"></span>
      </div>
    </header>
    <main class="content">
      <h1 class="title">ADD RECORD</h1>
      <div class="field field--invalid" style="left:1px;top:163px">Vet Name
        <svg class="alert" viewBox="0 0 22 22"><circle cx="11" cy="11" r="11" fill="#c40d0d"/><path d="M11 5v8M11 15.5v2" stroke="#fff" stroke-width="2.6"/></svg>
      </div>
      <div class="tooltip">Please Enter<br>Your Vet name</div>
      <div class="field" style="left:405px;top:163px">Vet Age</div>
      <div class="gender">Gender<div class="gender-options"><span class="radio"><i></i>Male</span><span class="radio"><i></i>Female</span></div></div>
      <div class="field" style="left:1px;top:234px">Weight</div>
      <div class="field" style="left:405px;top:234px">Color</div>
      <div class="field field--select" style="left:808px;top:234px">Number of Animales</div>
      <div class="field" style="left:1px;top:305px">Farm location</div>
      <div class="field" style="left:405px;top:305px">Reason</div>
      <button class="submit">SUBMIT</button>
      <table class="records">
        <colgroup><col style="width:256px"><col style="width:88px"><col style="width:85px"><col style="width:79px"><col style="width:78px"><col style="width:115px"><col style="width:140px"><col style="width:268px"><col style="width:81px"></colgroup>
        <thead><tr><th>Vet Name</th><th>Vet Age</th><th>Gender</th><th>Weight</th><th>Color</th><th>No.of animals</th><th>Location</th><th>Reason</th><th>Action</th></tr></thead>
        <tbody>
          <tr><td class="first">Cookie</td><td class="c">8</td><td class="l">Male</td><td class="c">20</td><td class="l">Brown</td><td class="c">1</td><td class="l">Allentown</td><td class="l">Lorem Ipsum is simply dummy</td><td><div class="actions"><svg viewBox="0 0 16 16" fill="none" stroke="#9cc43c" stroke-width="1.4"><path d="M13 9v5H2V3h5M6 10l1-3 6-6 2 2-6 6z"/></svg><span class="sep"></span><svg viewBox="0 0 16 16" fill="none" stroke="#e4531d" stroke-width="1.6"><path d="M2 4h12M6 4V2h4v2M4 4l1 11h6l1-11M7 7v5M9 7v5"/></svg></div></td></tr>
          <tr><td class="first">Lydia</td><td class="c">12</td><td class="l">Female</td><td class="c">15</td><td class="l">White</td><td class="c">3</td><td class="l">Orlando</td><td class="l">Contrary to popular belief</td><td><div class="actions"><svg viewBox="0 0 16 16" fill="none" stroke="#9cc43c" stroke-width="1.4"><path d="M13 9v5H2V3h5M6 10l1-3 6-6 2 2-6 6z"/></svg><span class="sep"></span><svg viewBox="0 0 16 16" fill="none" stroke="#e4531d" stroke-width="1.6"><path d="M2 4h12M6 4V2h4v2M4 4l1 11h6l1-11M7 7v5M9 7v5"/></svg></div></td></tr>
          <tr><td class="first">Cowles</td><td class="c">5</td><td class="l">Male</td><td class="c">31</td><td class="l">Black</td><td class="c">2</td><td class="l">Miami</td><td class="l">There are many variations of</td><td><div class="actions"><svg viewBox="0 0 16 16" fill="none" stroke="#9cc43c" stroke-width="1.4"><path d="M13 9v5H2V3h5M6 10l1-3 6-6 2 2-6 6z"/></svg><span class="sep"></span><svg viewBox="0 0 16 16" fill="none" stroke="#e4531d" stroke-width="1.6"><path d="M2 4h12M6 4V2h4v2M4 4l1 11h6l1-11M7 7v5M9 7v5"/></svg></div></td></tr>
          <tr><td class="first">Owens</td><td class="c">3</td><td class="l">Female</td><td class="c">25</td><td class="l">White</td><td class="c">6</td><td class="l">Fresno</td><td class="l">It is a long established fact</td><td><div class="actions"><svg viewBox="0 0 16 16" fill="none" stroke="#9cc43c" stroke-width="1.4"><path d="M13 9v5H2V3h5M6 10l1-3 6-6 2 2-6 6z"/></svg><span class="sep"></span><svg viewBox="0 0 16 16" fill="none" stroke="#e4531d" stroke-width="1.6"><path d="M2 4h12M6 4V2h4v2M4 4l1 11h6l1-11M7 7v5M9 7v5"/></svg></div></td></tr>
          <tr><td class="first">Beverly</td><td class="c">1</td><td class="l">Male</td><td class="c">10</td><td class="l">Brown</td><td class="c">5</td><td class="l">Mer Rouge</td><td class="l">Lorem Ipsum is simply dummy</td><td><div class="actions"><svg viewBox="0 0 16 16" fill="none" stroke="#9cc43c" stroke-width="1.4"><path d="M13 9v5H2V3h5M6 10l1-3 6-6 2 2-6 6z"/></svg><span class="sep"></span><svg viewBox="0 0 16 16" fill="none" stroke="#e4531d" stroke-width="1.6"><path d="M2 4h12M6 4V2h4v2M4 4l1 11h6l1-11M7 7v5M9 7v5"/></svg></div></td></tr>
          <tr><td class="first">Plumley</td><td class="c">20</td><td class="l">Female</td><td class="c">30</td><td class="l">Black</td><td class="c">3</td><td class="l">Sophia</td><td class="l">Contrary to popular belief</td><td><div class="actions"><svg viewBox="0 0 16 16" fill="none" stroke="#9cc43c" stroke-width="1.4"><path d="M13 9v5H2V3h5M6 10l1-3 6-6 2 2-6 6z"/></svg><span class="sep"></span><svg viewBox="0 0 16 16" fill="none" stroke="#e4531d" stroke-width="1.6"><path d="M2 4h12M6 4V2h4v2M4 4l1 11h6l1-11M7 7v5M9 7v5"/></svg></div></td></tr>
        </tbody>
      </table>
      <p class="copyright">Copyright © 2022 All Rights Reserved</p>
    </main>
  </section>

</div>
</body>
</html>
```